Card Design Project

A simple, funky, cool birth announcement card
Not corporate, but arty
Not childish nor girlish
No baby pictures

Text is tbc (eg name and date may change)

Front side: just the name "roos"
Should be easy to read

Back side text (in Dutch):

We vinden je nu al leuk!

20 JUNE 2013
Singapore

Dochter van Marieke Vos & Geert Bakker

Yangon, Myanmar
+95 1 48 7361
Skype: Marieke.Vos
Skype: Geert.Bakker

Size will be A6
Updates

Reason: Dear designers, At this stage we would like to have one or more designers to draft up the card (of which the final text is still tbd as the baby is yet to be born) using the typeface used on the left below (or similar!) of the newly added picture - in black - in fluorescent colours Can you get back to us in a few days? Thanks

Target Market(s)

Our funky friends in holland.

Industry/Entity Type

Baby

Requirements
Must have
• Colours, aswe are very happy to welcome this baby.
Something that makes it stand out from all other baby birth announcement cards

A6 size
Deadline 21 June
Printing will be on white (thick paper 250g)
Design for 5mm "bleedsides" all around
At least available in PDF (and other formats)
Nice to have
• We've recently moved from netherlands to Yangon
We could include the iconic thirikyaw pagoda

I would like for it to look like a cool party announcement

Include bright fluoriscent colours, including orange.
The enveloppe will be orange
Should not have
• Any baby stuff, soft pink dominance, childish stuff.

```html
<!DOCTYPE html>
<html lang="nl">
<head>
<meta charset="utf-8">
<title>Roos – geboortekaart</title>
<link rel="stylesheet" href="https://fonts.googleapis.com/css2?family=Comfortaa:wght@400;600;700&display=swap">
<style>
  :root {
    --stage: #f2f2f2;
    --paper-back: #ffd67e;
    --white: #ffffff;
    --date-blue: #3b5fd6;
    --parent-purple: #8a2dc4;
    --label-purple: #b04ad8;
    --orange: #ff6a00;
    --amber: #ffb300;
    --yellow: #ffe11a;
    --green: #3fd14a;
    --teal: #13b3b8;
    --blue: #2f5fe0;
    --violet: #7a2fd6;
    --magenta: #ff2fa8;
    --red: #ff2a3a;
    --card-w: 560px;
    --card-h: 396px;
  }
  * { box-sizing: border-box; margin: 0; padding: 0; }
  html, body {
    width: 1200px; height: 900px; overflow: hidden;
    background: var(--stage);
    font-family: "Comfortaa", sans-serif;
  }
  .card {
    position: absolute;
    width: var(--card-w); height: var(--card-h);
    overflow: hidden;
    box-shadow: 0 6px 18px rgba(0,0,0,.25);
  }
  .card--front { left: 40px; top: 40px; }
  .card--back { left: 600px; top: 464px; background: var(--paper-back); }

  .streaks {
    position: absolute; inset: 0;
    background:
      repeating-linear-gradient(90deg, rgba(255,255,255,.10) 0 3px, rgba(0,0,0,.06) 3px 7px, rgba(255,255,255,0) 7px 13px),
      linear-gradient(180deg, rgba(255,255,255,0) 55%, rgba(255,120,0,.35) 100%),
      linear-gradient(90deg, var(--orange) 0%, var(--amber) 14%, var(--yellow) 24%, var(--green) 34%, var(--teal) 46%, var(--blue) 58%, var(--violet) 70%, var(--magenta) 84%, var(--red) 100%);
  }

  .pagoda {
    position: absolute; left: 0; bottom: 0;
    width: 360px; height: 250px;
  }

  .name {
    position: absolute; left: 0; right: 0; top: 46px;
    text-align: center;
    font-size: 118px; font-weight: 700; letter-spacing: 6px;
    text-transform: uppercase;
    color: var(--white);
    text-shadow: 0 0 6px rgba(255,255,255,.8), 2px 3px 0 rgba(120,30,150,.35);
  }

  .band {
    position: absolute; left: 0; top: 0; right: 0; height: 140px;
  }
  .band .streaks {
    background:
      repeating-linear-gradient(90deg, rgba(255,255,255,.10) 0 3px, rgba(0,0,0,.06) 3px 7px, rgba(255,255,255,0) 7px 13px),
      linear-gradient(180deg, rgba(255,214,126,0) 60%, var(--paper-back) 100%),
      linear-gradient(90deg, var(--orange) 0%, var(--amber) 12%, var(--red) 24%, var(--violet) 36%, var(--blue) 48%, var(--teal) 58%, var(--green) 66%, var(--magenta) 80%, var(--red) 92%, var(--orange) 100%);
  }
  .headline {
    position: relative;
    padding: 14px 0 0 8px;
    font-size: 41px; font-weight: 700; line-height: 1.05;
    text-transform: uppercase;
    color: var(--white);
  }
  .details {
    position: absolute; left: 10px; top: 144px; right: 10px;
    text-transform: uppercase;
  }
  .date { font-size: 21px; font-weight: 600; color: var(--date-blue); }
  .place { font-size: 19px; color: var(--white); margin-top: 2px; }
  .parents {
    margin-top: 14px;
    font-size: 31px; line-height: 1.05; font-weight: 600;
    color: var(--parent-purple);
  }
  .contact { margin-top: 12px; font-size: 14px; line-height: 1.65; }
  .contact .city { color: var(--date-blue); font-weight: 600; }
  .contact .phone, .contact .handle { color: var(--white); }
  .contact .label { color: var(--label-purple); font-weight: 600; }
</style>
</head>
<body>

<section class="card card--front">
  <div class="streaks" role="img" aria-label="Kleurrijke lichtstrepen als achtergrond"></div>
  <svg class="pagoda" viewBox="0 0 360 250" role="img" aria-label="Silhouet van de thirikyaw pagode in oranje gloed">
    <defs>
      <radialGradient id="pagodaGlow" cx="0.3" cy="1" r="0.9">
        <stop offset="0" stop-color="#ff5a00"/>
        <stop offset="0.55" stop-color="#ff9a00" stop-opacity="0.85"/>
        <stop offset="1" stop-color="#ffd400" stop-opacity="0"/>
      </radialGradient>
    </defs>
    <rect width="360" height="250" fill="url(#pagodaGlow)"/>
  </svg>
  <h1 class="name">roos</h1>
</section>

<section class="card card--back">
  <div class="band">
    <div class="streaks" role="img" aria-label="Kleurrijke lichtstrepen als achtergrond"></div>
    <h2 class="headline">We vinden<br>je nu al leuk</h2>
  </div>
  <div class="details">
    <p class="date">20 June 2013</p>
    <p class="place">Singapore</p>
    <p class="parents">Dochter van<br>Marieke Vos &amp; Geert Bakker</p>
    <div class="contact">
      <p class="city">Yangon, Myanmar</p>
      <p class="phone">+95 1 48 7361</p>
      <p><span class="label">Skype:</span> <span class="handle">Marieke.Vos</span></p>
      <p><span class="label">Skype:</span> <span class="handle">Geert.Bakker</span></p>
    </div>
  </div>
</section>

</body>
</html>
```